Attorney Website Design

I need a top quality attorney website layout designed. Here are some examples of what I feel are great websites:
http://www.quellmarstonseparationlaw.com/
http://www.vandriclegalgroup.com/
http://www.pobelaw.com/
http://www.harrowvaleaccusedcounselhq.com/
http://www.tzlegal.com/
http://www.brookhollowtrialjusticeoffice.com/
http://www.orvynchargedcounsel.com/
http://www.tzlegal.com/
What we like about these sites:
• The different layers
• Subtle designs, textures, curves
• 3 dimensional
• Floating effects
• Prominent phone number
• Location of Areas of Practice
• Request A Consultation Prominent
• Right side bar with practice areas
• Badges
• Clear Calls to Action
• Dynamic/Staying Top navigation when you scroll
The project will be for a home page and then also an interior page (should be similar to home page).
Updates
I want to make it understood I am looking for a design which is not a typical "template" site which I can find anywhere for $50. This budget and project is for a "Custom" website design. Please submit designs similar in quality to the samples links I have posted. Creativity is a MUST! The best way to explain this is, I want a design that I can feel it unique and original, not something that looks like 95% of all websites out there.
Neil
I just wanted everyone to know that so far I am not to pleased with any of the designs. I am not looking for cut/pasting of other peoples websites but ORIGINAL and CREATIVE work.
Reason: Weekend + Holiday extension.
Reason: Need more designs
Industry/Entity Type
Attorney

```html
<!DOCTYPE html>
<html lang="en">
<head>
<meta charset="utf-8">
<title>Halverne Attorneys</title>
<link href="https://fonts.googleapis.com/css2?family=Dosis:wght@400;500;600&family=Open+Sans:wght@400;600;700&family=Ubuntu:wght@400&display=swap" rel="stylesheet">
<style>
:root{
  --navy:#0b2147;
  --nav-blue:#1e5a8c;
  --nav-active:#2b78b4;
  --accent:#1f5a9a;
  --link:#1d5fa8;
  --paper:#f3f4f6;
  --panel:#f8f9fb;
  --text:#444;
  --heading:#222;
  --footer:#3d3e40;
  --footer-deep:#262728;
  --line:#d8dbe0;
}
*{margin:0;padding:0;box-sizing:border-box}
html,body{width:719px;height:1200px;overflow:hidden}
body{position:relative;background:var(--paper);font-family:"Open Sans",sans-serif;color:var(--text)}
.abs{position:absolute}
.topbar{left:0;top:0;width:719px;height:19px;background:#e9eaec;text-align:center;font:500 13px/19px "Dosis",sans-serif;color:#333;padding-left:34px}
.masthead{left:0;top:19px;width:719px;height:199px;background:var(--navy)}
.logo-tab{left:86px;top:11px;width:154px;height:52px}
.logo-name{left:86px;top:17px;width:154px;text-align:center;font:500 17.5px "Dosis",sans-serif;color:#333}
.cta{left:495px;top:29px;width:146px;height:25px;border-radius:3px;background:linear-gradient(#9fdcf7,#5fbde9);border:1px solid #cfeefc;font:500 13.5px/23px "Dosis",sans-serif;color:#0b2c55;text-align:center}
.nav{left:78px;top:74px;width:562px;height:28px;background:linear-gradient(#2767a0,#1a4f82);display:flex}
.nav a{font:500 9.2px/28px "Dosis",sans-serif;color:#fff;text-decoration:none;padding:0 7.6px;border-right:1px solid #154473;text-transform:uppercase;letter-spacing:.1px}
.nav a.active{background:var(--nav-active)}
.nav a:last-child{border-right:0;flex:1;text-align:center}
.hero{left:78px;top:102px;width:562px;height:220px;background:linear-gradient(90deg,#3a2a1e 0%,#6b4a2c 40%,#5a3b22 70%,#3d2a1b 100%)}
.hero-caption{left:78px;top:300px;width:562px;height:22px;background:rgba(0,0,0,.55);font:400 12.4px/22px "Ubuntu",sans-serif;color:#fff;padding-left:19px}
.arrow{width:18px;height:25px;background:#e9eaec;border:1px solid #bbb}
.area-photo{width:96px;height:96px;border-radius:50%;border:3px solid #2a2a2a;box-shadow:0 0 0 3px #fff}
.area-num{width:24px;height:24px;border-radius:50%;background:var(--navy);border:2px solid #fff;color:#fff;font:500 14px/20px "Dosis",sans-serif;text-align:center}
.area-label{width:140px;text-align:center;font:500 13px "Dosis",sans-serif;color:#222}
.content{left:78px;top:487px;width:388px;height:389px;background:var(--panel);box-shadow:0 0 6px rgba(0,0,0,.08)}
.sidebar{left:466px;top:487px;width:174px;height:389px;background:linear-gradient(90deg,#e4e7ec,#f1f2f4)}
h2{font:600 14.5px "Dosis",sans-serif;color:var(--heading)}
h2 span{color:var(--accent)}
.welcome{left:91px;top:497px}
.copy{left:91px;top:529px;width:352px;font-size:8.3px;line-height:12.8px;color:#555}
.copy p{margin-bottom:6px}
.copy a{color:var(--link);text-decoration:none}
.video{left:91px;top:693px;width:348px;height:174px;border:2px solid #ccc;background:#fff}
.video-frame{left:2px;top:2px;width:340px;height:158px;background:linear-gradient(90deg,#8a6a3c,#c9b48a 50%,#a78858)}
.video-bar{left:0;top:161px;width:344px;height:9px;background:#e8e8e8;font-size:5.5px;line-height:9px;color:#222}
.side-head{left:480px;top:500px}
.practice{left:480px;top:529px;list-style:none}
.practice li{height:19.7px;font-size:7.4px;color:#333;display:flex;align-items:center;gap:9px;text-transform:uppercase}
.practice li:after{content:"";position:absolute}
.consult{left:466px;top:690px;width:163px;height:178px}
.consult-title{left:466px;top:692px;width:163px;text-align:center;font:500 16.5px/19px "Dosis",sans-serif;color:#fff;letter-spacing:.4px}
.field{left:486px;width:125px;height:16px;background:#fff;border:1px solid #d6d6d6;font-size:6px;line-height:14px;color:#aaa;padding-left:5px}
.submit{left:510px;top:833px;width:74px;height:17px;background:var(--accent);border:1px solid #0f3a6a;color:#fff;font:700 8.5px/15px "Open Sans",sans-serif;text-align:center}
.quote{width:239px;height:76px;background:#fff;box-shadow:0 1px 4px rgba(0,0,0,.12)}
.quote p{position:absolute;left:35px;top:12px;width:196px;font-size:7.2px;line-height:13.4px;color:#555}
.qmark{position:absolute;left:12px;top:6px;font:700 30px/30px Georgia,serif;color:#ddd}
.avatar{width:44px;height:44px;border-radius:50%;background:radial-gradient(#d3bfa9,#9a8575);border:2px solid #fff;box-shadow:0 0 3px rgba(0,0,0,.2)}
.who{font-size:10px;color:var(--link);font-weight:600}
.who small{display:block;font-size:7.6px;color:#666;font-weight:400;margin-top:1px}
.footer-art{left:0;top:960px}
.f-head{font:400 11.5px "Dosis",sans-serif;color:#fff;letter-spacing:.3px;text-transform:uppercase}
.f-divider{top:1034px;width:1px;height:138px;background:#555}
.quicklinks{left:79px;top:1083px;list-style:none;font-size:7.2px;line-height:10.3px;color:#fff}
.quicklinks li:before{content:">  ";white-space:pre}
.contact-list{left:203px;top:1086px;font-size:7.2px;line-height:9.8px;color:#fff}
.contact-list .row{display:flex;gap:9px;margin-bottom:6px}
.contact-list svg{flex:none}
.nl-field{left:375px;width:121px;height:15px;background:#fff;font-style:italic;font-size:7.2px;line-height:15px;color:#333;padding-left:5px;border:1px solid #999}
.nl-submit{left:376px;top:1149px;width:58px;height:16px;background:var(--accent);border-radius:2px;color:#fff;font:700 8.6px/16px "Open Sans",sans-serif;padding-left:6px}
.like{left:545px;top:1086px;width:95px;height:17px;background:#fff;border-radius:2px;font-size:7.2px;line-height:17px;text-align:center;color:#222}
.social{top:1111px;width:21px;height:21px;border-radius:3px}
.copyright{left:0;top:1173px;width:719px;height:27px;background:var(--footer-deep);color:#ddd;font-size:7.4px;line-height:27px;text-align:center}
</style>
</head>
<body>
<div class="abs topbar">Call Us: 123-456-7890</div>
<div class="abs masthead"></div>

<svg class="abs logo-tab" viewBox="0 0 154 52" aria-hidden="true">
  <path d="M0 0H154V40L77 52L0 40Z" fill="#fff" stroke="#d6d6d6"/>
</svg>
<div class="abs logo-name">Halverne Attorneys</div>
<div class="abs cta">Request A Consultation</div>

<nav class="abs nav">
  <a class="active">Home</a><a>About Us</a><a>Attorneys &amp; Staff</a><a>Practice Areas</a><a>Testimonials</a><a>Video Center</a><a>Free Consultation</a><a>Contact Us</a>
</nav>

<div class="abs hero" role="img" aria-label="Three attorneys standing in front of library bookshelves"></div>
<div class="abs hero-caption">Lorem ipsum dolor sit amet, consect adipiscing elit, sed diam nonuummy eeuismod tincidunt</div>
<div class="abs arrow" style="left:74px;top:190px"><svg width="16" height="23" viewBox="0 0 16 23"><path d="M10 6L5 11.5L10 17" fill="none" stroke="#333" stroke-width="2"/></svg></div>
<div class="abs arrow" style="left:627px;top:190px"><svg width="16" height="23" viewBox="0 0 16 23"><path d="M6 6L11 11.5L6 17" fill="none" stroke="#333" stroke-width="2"/></svg></div>

<div class="abs area-photo" style="left:142px;top:343px;background:radial-gradient(#d9a970,#7a4a22)" role="img" aria-label="Gavel and handcuffs"></div>
<div class="abs area-num" style="left:126px;top:383px">1</div>
<div class="abs area-label" style="left:120px;top:450px">Criminal Defense</div>
<div class="abs area-photo" style="left:310px;top:343px;background:radial-gradient(#f4f4f4,#bfb8b0)" role="img" aria-label="Couple turned away from each other"></div>
<div class="abs area-num" style="left:294px;top:383px">2</div>
<div class="abs area-label" style="left:290px;top:450px">Family Law</div>
<div class="abs area-photo" style="left:490px;top:343px;background:radial-gradient(#c9d9ec,#4d74a8)" role="img" aria-label="Arm in a sling"></div>
<div class="abs area-num" style="left:475px;top:383px">3</div>
<div class="abs area-label" style="left:472px;top:450px">Personal Injury</div>

<div class="abs content"></div>
<div class="abs sidebar"></div>

<h2 class="abs welcome">Welcome to <span>Halverne Attorneys</span></h2>
<div class="abs copy">
  <p>Lorem ipsum dolor sit amet, consectetuer adipiscing elit, sed diam nonummy nibh euismod tincidunt ut laoreet dolore magna aliquam erat volutpat. Ut wisi enim ad minim erekr jkerjkekr lerelr ...</p>
  <p>Lorem ipsum dolor sit amet, consectetuer adipiscing elit, sed diam nonummy nibh euismod tincidunt ut laoreet dolore magna aliquam erat volutpat. Ut wisi enim ad minim veniam, quis nostrud exerci tation ullamcorper suscipit lobortis nisl ut aliquip ex ea commodo consequat Rerjekrje tuer adipiscing elit, sed diam nonummy nibh euismod tincidunt ut laoreet dolore magna aliquam erat volutpat. Ut wisi enim ad minim veniam, quis nostrud exerci tation ullamc.</p>
  <p>Lorem ipsum dolor sit amet, consectetuer adipiscing elit, sed diam nonummy nibh euismod tincidunt ut laoreet dolore magna aliquam erat volutpat.... <a>READ MORE</a></p>
</div>

<div class="abs video">
  <div class="abs video-frame" role="img" aria-label="Attorney leaning on a bookshelf, video still"></div>
  <svg class="abs" style="left:147px;top:63px" width="40" height="30" viewBox="0 0 40 30"><rect width="40" height="30" rx="4" fill="rgba(0,0,0,.45)"/><path d="M15 8L27 15L15 22Z" fill="#fff"/></svg>
  <div class="abs video-bar">
    <span style="position:absolute;left:3px">&#9654;</span>
    <span style="position:absolute;left:18px">00:00</span>
    <span style="position:absolute;left:38px;top:3px;width:280px;height:3px;background:#bbb"></span>
    <span style="position:absolute;left:290px">00:00</span>
    <span style="position:absolute;left:312px;top:3px;width:16px;height:3px;background:#666"></span>
  </div>
</div>

<h2 class="abs side-head">Practice <span>Areas</span></h2>
<svg class="abs" style="left:480px;top:521px" width="150" height="2"><line x1="0" y1="1" x2="150" y2="1" stroke="#c8cdd5" stroke-dasharray="2 2"/></svg>
<ul class="abs practice">
  <li><svg width="9" height="9" viewBox="0 0 9 9"><circle cx="4.5" cy="4.5" r="3.6" fill="none" stroke="#2a5e96"/><path d="M2.6 4.6L4.2 6L8.5 1.2" fill="none" stroke="#2a5e96" stroke-width="1.3"/></svg>DUI Defense</li>
  <li><svg width="9" height="9" viewBox="0 0 9 9"><circle cx="4.5" cy="4.5" r="3.6" fill="none" stroke="#2a5e96"/><path d="M2.6 4.6L4.2 6L8.5 1.2" fill="none" stroke="#2a5e96" stroke-width="1.3"/></svg>Serious Vehicular Crimes</li>
  <li><svg width="9" height="9" viewBox="0 0 9 9"><circle cx="4.5" cy="4.5" r="3.6" fill="none" stroke="#2a5e96"/><path d="M2.6 4.6L4.2 6L8.5 1.2" fill="none" stroke="#2a5e96" stroke-width="1.3"/></svg>Theft Crimes</li>
  <li><svg width="9" height="9" viewBox="0 0 9 9"><circle cx="4.5" cy="4.5" r="3.6" fill="none" stroke="#2a5e96"/><path d="M2.6 4.6L4.2 6L8.5 1.2" fill="none" stroke="#2a5e96" stroke-width="1.3"/></svg>Drug Crimes</li>
  <li><svg width="9" height="9" viewBox="0 0 9 9"><circle cx="4.5" cy="4.5" r="3.6" fill="none" stroke="#2a5e96"/><path d="M2.6 4.6L4.2 6L8.5 1.2" fill="none" stroke="#2a5e96" stroke-width="1.3"/></svg>Sex Crimes</li>
  <li><svg width="9" height="9" viewBox="0 0 9 9"><circle cx="4.5" cy="4.5" r="3.6" fill="none" stroke="#2a5e96"/><path d="M2.6 4.6L4.2 6L8.5 1.2" fill="none" stroke="#2a5e96" stroke-width="1.3"/></svg>High School and College Cases</li>
  <li><svg width="9" height="9" viewBox="0 0 9 9"><circle cx="4.5" cy="4.5" r="3.6" fill="none" stroke="#2a5e96"/><path d="M2.6 4.6L4.2 6L8.5 1.2" fill="none" stroke="#2a5e96" stroke-width="1.3"/></svg>Other Offenses</li>
  <li><svg width="9" height="9" viewBox="0 0 9 9"><circle cx="4.5" cy="4.5" r="3.6" fill="none" stroke="#2a5e96"/><path d="M2.6 4.6L4.2 6L8.5 1.2" fill="none" stroke="#2a5e96" stroke-width="1.3"/></svg>Expungement</li>
</ul>

<svg class="abs consult" viewBox="0 0 163 178" aria-hidden="true">
  <defs><linearGradient id="band" x1="0" y1="0" x2="0" y2="1"><stop offset="0" stop-color="#2a6aa8"/><stop offset="1" stop-color="#123e72"/></linearGradient></defs>
  <path d="M1 8H162V160L81.5 177L1 160Z" fill="#fff" stroke="#d2d6dc"/>
  <path d="M0 0H163V30L81.5 42L0 30Z" fill="url(#band)"/>
</svg>
<div class="abs consult-title">READY TO FREE<br>CONSULTATION</div>
<div class="abs field" style="top:750px">First Name</div>
<div class="abs field" style="top:778px">Last Name</div>
<div class="abs field" style="top:805px">Email</div>
<div class="abs submit">SUBMIT NOW</div>

<div class="abs quote" style="left:106px;top:888px"><span class="qmark">&#8220;</span><p>Lorem ipsum dolor sit amet, consectetuer adipiscinge sed diam nonummy nibh euismod tincidunt ut laoreet dolore magna aliquam erat volutpat. Ut wisi enim ad minim veniam, quis nostrud exerci tation.</p></div>
<div class="abs quote" style="left:368px;top:888px"><span class="qmark">&#8220;</span><p>Lorem ipsum dolor sit amet, consectetuer adipiscinge sed diam nonummy nibh euismod tincidunt ut laoreet dolore magna aliquam erat volutpat. Ut wisi enim ad minim veniam, quis nostrud exerci tation.</p></div>

<svg class="abs footer-art" width="719" height="213" viewBox="0 0 719 213" aria-hidden="true">
  <path d="M0 22C60 70 200 85 360 80C500 76 640 40 719 18V213H0Z" fill="#1d55a0"/>
  <path d="M0 24C70 80 220 95 360 88C510 82 640 55 719 32V213H0Z" fill="#f3f4f6"/>
  <path d="M0 28C40 70 150 84 300 82C460 80 620 60 719 40V213H0Z" fill="#2a2b2d"/>
  <path d="M0 60C80 80 210 86 360 84C500 82 630 62 719 48V213H0Z" fill="var(--footer)"/>
</svg>

<div class="abs avatar" style="left:110px;top:975px" role="img" aria-label="Client portrait"></div>
<div class="abs who" style="left:161px;top:984px">Lorem Ipsum<small>Manager</small></div>
<div class="abs avatar" style="left:372px;top:975px" role="img" aria-label="Client portrait"></div>
<div class="abs who" style="left:422px;top:984px">Lorem Ipsum<small>Director</small></div>

<div class="abs f-divider" style="left:178px"></div>
<div class="abs f-divider" style="left:349px"></div>
<div class="abs f-divider" style="left:522px"></div>

<div class="abs f-head" style="left:79px;top:1064px">Quick Link</div>
<ul class="abs quicklinks">
  <li>Home</li><li>Attorneys &amp; Staff</li><li>Practice Areas</li><li>Testimonials</li><li>Video Center</li><li>Free Consultation</li><li>About Us</li><li>Contact Us</li>
</ul>

<div class="abs f-head" style="left:203px;top:1064px">Contact Information</div>
<div class="abs contact-list">
  <div class="row"><svg width="9" height="11" viewBox="0 0 9 11"><path d="M4.5 10.5C1.5 6.5 1 5.2 1 4A3.5 3.5 0 0 1 8 4C8 5.2 7.5 6.5 4.5 10.5Z" fill="none" stroke="#fff"/><circle cx="4.5" cy="4" r="1.2" fill="#fff"/></svg><span>Lorem ipsum dolor sit amet,<br>cwensectetuer adipiscinge<br>sed diam nonummy.</span></div>
  <div class="row" style="margin-top:4px"><svg width="10" height="10" viewBox="0 0 10 10"><path d="M2 0.8L3.8 3L2.8 4.2C3.5 5.8 4.5 6.8 5.8 7.3L7 6.2L9.2 8L8 9.6C4 9.2 0.8 6 0.4 2Z" fill="#fff"/></svg><span>123-456-7890</span></div>
  <div class="row" style="margin-top:7px"><svg width="10" height="8" viewBox="0 0 10 8"><rect x="0.5" y="0.5" width="9" height="7" fill="none" stroke="#fff"/><path d="M0.5 0.5L5 4.5L9.5 0.5" fill="none" stroke="#fff"/></svg><span>info@halverneattorneys.com</span></div>
  <div class="row" style="margin-top:7px"><svg width="10" height="10" viewBox="0 0 10 10"><rect x="2" y="0.5" width="6" height="3" fill="none" stroke="#fff"/><rect x="0.5" y="3.5" width="9" height="4.5" fill="#fff"/><rect x="2" y="6.5" width="6" height="3" fill="#fff" stroke="#3d3e40" stroke-width=".6"/></svg><span>123-456-7890</span></div>
</div>

<div class="abs f-head" style="left:375px;top:1064px">Newsletter Signup</div>
<div class="abs nl-field" style="top:1085px">First Name</div>
<div class="abs nl-field" style="top:1105px">Last Name</div>
<div class="abs nl-field" style="top:1126px">Email Address</div>
<div class="abs nl-submit">SUBMIT <svg width="10" height="10" viewBox="0 0 10 10" style="vertical-align:-1px;margin-left:2px"><circle cx="5" cy="5" r="5" fill="#fff"/><path d="M4 2.8L6.6 5L4 7.2Z" fill="#1f5a9a"/></svg></div>

<div class="abs f-head" style="left:546px;top:1064px">Followus</div>
<div class="abs like">Like me on Linkwall</div>
<div class="abs social" style="left:545px;background:#3b5a9a"></div>
<div class="abs social" style="left:571px;background:#2aa3e0"></div>
<div class="abs social" style="left:597px;background:#1a6fa8"></div>
<div class="abs social" style="left:623px;background:#d2432f"></div>

<div class="abs copyright">Copyright@2014. Halverne Attorneys, All Rights Reserved.</div>
</body>
</html>
```